Landscape design build company door flyer

I would like this flyer to convey a high-level of professionalism for a company that is excellent with communication with their clients as well as a company that does incredible installations

Went on vacation/holiday

```html
<!DOCTYPE html>
<html lang="en">
<head>
<meta charset="UTF-8">
<title>Stillwater Builders – Outdoor Living Spaces Flyer</title>
<link href="https://fonts.googleapis.com/css2?family=Montserrat:wght@400;500;600;700;800;900&display=swap" rel="stylesheet">
<style>
  :root{
    --yellow:#fdbb00;
    --black:#141414;
    --white:#ffffff;
    --navy:#153a4a;
    --ink:#1a1a1a;
    --caption:rgba(12,12,12,.88);
  }
  *{margin:0;padding:0;box-sizing:border-box;}
  html,body{width:1200px;height:849px;overflow:hidden;background:var(--white);}
  body{font-family:"Montserrat",sans-serif;color:var(--ink);}
  .flyer{position:relative;width:1200px;height:849px;background:var(--white);overflow:hidden;}

  /* hero */
  .hero{position:absolute;left:38px;top:38px;width:1123px;height:342px;border-radius:22px;overflow:hidden;
    background:linear-gradient(100deg,#1c1d1a 0%,#23241f 30%,#2a2b2a 55%,#262728 75%,#1d1e20 100%);}
  .hero::after{content:"";position:absolute;inset:0;background:linear-gradient(180deg,rgba(0,0,0,.15),rgba(0,0,0,.45));}
  .brand-tab{position:absolute;left:431px;top:38px;width:327px;height:138px;background:var(--white);
    border-radius:0 0 10px 10px;z-index:2;display:flex;flex-direction:column;align-items:center;justify-content:flex-end;padding-bottom:18px;}
  .brand-mark{width:34px;height:34px;border-radius:50%;background:var(--navy);margin-bottom:20px;}
  .brand-name{font-weight:700;font-size:21px;color:var(--navy);letter-spacing:.2px;line-height:1;}
  .brand-tagline{font-weight:700;font-size:11.5px;color:var(--navy);margin-top:6px;letter-spacing:.1px;line-height:1;}

  .headline{position:absolute;left:0;width:1200px;text-align:center;z-index:2;font-weight:900;
    letter-spacing:-4px;line-height:1;}
  .headline.top{top:206px;font-size:84px;color:var(--yellow);padding-right:20px;}
  .headline.bottom{top:280px;font-size:84px;color:var(--white);}

  /* services */
  .services-pill{position:absolute;left:0;top:400px;width:328px;height:63px;background:var(--yellow);
    border-radius:0 32px 32px 0;display:flex;align-items:center;padding-left:45px;}
  .services-pill h2{font-weight:800;font-size:29px;color:var(--black);letter-spacing:.2px;}

  .tile{position:absolute;width:211px;height:132px;overflow:hidden;}
  .tile .photo{position:absolute;inset:0;}
  .tile .label{position:absolute;left:0;right:0;bottom:0;height:28px;background:var(--caption);
    color:var(--white);font-weight:700;font-size:11px;letter-spacing:-.3px;display:flex;align-items:center;justify-content:center;}
  .c1{left:295px;} .c1{left:295px;}
  .photo.patio{background:linear-gradient(180deg,#8fa7b8 0%,#5d6a4f 45%,#4a4a40 100%);}
  .photo.driveway{background:linear-gradient(180deg,#6b6a66 0%,#9a8670 30%,#8a4a22 50%,#a89a8a 100%);}
  .photo.walls{background:linear-gradient(180deg,#4d5a3a 0%,#6f5444 25%,#6e6c68 55%,#4f4e4b 100%);}
  .photo.decks{background:linear-gradient(180deg,#5f8b4a 0%,#7a4a2a 45%,#8e4f2c 75%,#6a3a20 100%);}
  .photo.pools{background:linear-gradient(180deg,#e6ebee 0%,#c9c3b8 40%,#6fb8c4 70%,#3f9db0 100%);}
  .photo.fire{background:linear-gradient(180deg,#566346 0%,#9d9790 35%,#8a847c 65%,#565a4a 100%);}

  /* services list */
  .list-card{position:absolute;left:733px;top:402px;width:429px;height:351px;background:var(--yellow);border-radius:20px;}
  .list-card h3{position:absolute;left:41px;top:15px;font-weight:700;font-size:21.5px;line-height:26px;color:var(--black);letter-spacing:.2px;}
  .item{position:absolute;font-weight:500;font-size:13px;line-height:18px;color:var(--black);padding-left:14px;}
  .item::before{content:"";position:absolute;left:0;top:6px;width:6px;height:6px;border-radius:50%;background:var(--black);}
  .col-a{left:38px;} .col-b{left:249px;width:150px;}

  /* footer */
  .footer{position:absolute;left:0;top:769px;width:1200px;height:80px;background:var(--black);}
  .offer{position:absolute;left:44px;top:17px;width:558px;height:44px;background:var(--yellow);border-radius:6px;
    display:flex;align-items:center;justify-content:center;font-weight:900;font-size:25.5px;color:var(--black);letter-spacing:.3px;}
  .phone-icon{position:absolute;left:641px;top:17px;width:50px;height:50px;}
  .call-label{position:absolute;left:711px;top:14px;font-weight:400;font-size:17px;color:var(--white);}
  .call-number{position:absolute;left:711px;top:38px;font-weight:700;font-size:24px;color:var(--white);}
  .contact-icon{position:absolute;width:14px;height:14px;}
  .address{position:absolute;left:966px;top:11px;font-weight:600;font-size:13.5px;line-height:18px;color:var(--white);}
  .web{position:absolute;left:966px;top:52px;font-weight:400;font-size:11.5px;color:var(--white);}
</style>
</head>
<body>
<main class="flyer">

  <section class="hero" role="img" aria-label="Photo of a backyard at dusk with stone retaining walls, wooden fence and a house with garage"></section>

  <header class="brand-tab">
    <span class="brand-mark"></span>
    <span class="brand-name">STILLWATER BUILDERS</span>
    <span class="brand-tagline">OUTDOOR LIVING SPACES</span>
  </header>

  <h1>
    <span class="headline top">IT’S TIME TO</span>
    <span class="headline bottom">DISCOVER YOUR ZEN</span>
  </h1>

  <div class="services-pill"><h2>OUR SERVICES</h2></div>

  <div class="tile" style="left:46px;top:481px;">
    <div class="photo patio" role="img" aria-label="Photo of a paver patio with pergola and outdoor seating"></div>
    <div class="label">PAVER PATIOS</div>
  </div>
  <div class="tile" style="left:266px;top:481px;">
    <div class="photo driveway" role="img" aria-label="Photo of a paver driveway in front of wooden garage doors"></div>
    <div class="label">PAVER DRIVEWAYS</div>
  </div>
  <div class="tile" style="left:485px;top:481px;">
    <div class="photo walls" role="img" aria-label="Photo of stone retaining walls with steps"></div>
    <div class="label">RETAINING WALLS</div>
  </div>
  <div class="tile" style="left:45px;top:621px;">
    <div class="photo decks" role="img" aria-label="Photo of a wooden deck with railings and patio chairs"></div>
    <div class="label">DECKS &amp; RAILINGS</div>
  </div>
  <div class="tile" style="left:264px;top:621px;">
    <div class="photo pools" role="img" aria-label="Photo of a modern home with a swimming pool"></div>
    <div class="label">POOLS</div>
  </div>
  <div class="tile" style="left:484px;top:621px;">
    <div class="photo fire" role="img" aria-label="Photo of a stone outdoor fireplace with firewood"></div>
    <div class="label">FIREPITS &amp; FIREPLACES</div>
  </div>

  <aside class="list-card">
    <h3>SOME OF THE SERVICES<br>WE PROVIDE:</h3>
    <span class="item col-a" style="top:76px;">Landscape design</span>
    <span class="item col-a" style="top:103px;">Landscaping</span>
    <span class="item col-a" style="top:129px;">Hardscaping</span>
    <span class="item col-a" style="top:154px;">Retaining wall design</span>
    <span class="item col-a" style="top:180px;">Retaining walls</span>
    <span class="item col-a" style="top:207px;">Pool designs</span>
    <span class="item col-a" style="top:234px;">Driveways</span>
    <span class="item col-a" style="top:259px;">Firepits</span>
    <span class="item col-a" style="top:285px;">Pavers</span>
    <span class="item col-a" style="top:311px;">Deck designs</span>

    <span class="item col-b" style="top:76px;">Luxury outdoor elements</span>
    <span class="item col-b" style="top:115px;">Outdoor living spaces</span>
    <span class="item col-b" style="top:154px;">Patio designs</span>
    <span class="item col-b" style="top:180px;">Outdoor lighting</span>
    <span class="item col-b" style="top:207px;">Outdoor kitchen spaces</span>
    <span class="item col-b" style="top:253px;">Fencing</span>
    <span class="item col-b" style="top:282px;">Fireplaces</span>
    <span class="item col-b" style="top:311px;">Sheds</span>
  </aside>

  <footer class="footer">
    <div class="offer">GET 10% OFF YOUR FIRST PROJECT</div>

    <svg class="phone-icon" viewBox="0 0 50 50" fill="none" stroke="var(--yellow)" stroke-width="2.6" stroke-linejoin="round" stroke-linecap="round">
      <path d="M10 6 L17 5 L21 16 L16 20 Q20 30 30 35 L34 30 L45 34 L44 41 Q40 47 32 45 Q14 39 5 18 Q4 10 10 6 Z"/>
      <path d="M27 10 Q37 12 40 22"/>
      <path d="M28 3 Q44 6 47 22"/>
    </svg>
    <div class="call-label">Call Us Now!</div>
    <div class="call-number">(206) 555-0142</div>

    <svg class="contact-icon" style="left:943px;top:15px;" viewBox="0 0 14 14" fill="none" stroke="var(--yellow)" stroke-width="1.2">
      <path d="M7 13 C3 8 2.5 6.5 2.5 5 A4.5 4.5 0 0 1 11.5 5 C11.5 6.5 11 8 7 13 Z"/>
      <circle cx="7" cy="5" r="1.6"/>
    </svg>
    <div class="address">1820 Cedar Ridge Lane<br>Maple Falls, WA 98000</div>

    <svg class="contact-icon" style="left:942px;top:52px;" viewBox="0 0 14 14" fill="none" stroke="var(--yellow)" stroke-width="1">
      <circle cx="7" cy="7" r="6"/>
      <ellipse cx="7" cy="7" rx="2.6" ry="6"/>
      <path d="M1 7 H13 M2 4 H12 M2 10 H12"/>
    </svg>
    <div class="web">www.stillwaterbuilders.com</div>
  </footer>

</main>
</body>
</html>
```